Business Card Design Project

We need a double-sided business card design for our e-commerce company. Be as creative as you can.

Reason: Change of logo

Target Market(s)

Business owners

Industry/Entity Type

E-Commerce

Requirements
Must have
• Name (editable)
Mobile number -editable
www.velbiro.com - MUST STAND OUT ALONE
Office address:
27 Marlow Street
#09-04 Westbrook Tower
Singapore 048216

```html
<!DOCTYPE html>
<html lang="en">
<head>
<meta charset="utf-8">
<title>Velbiro Business Card</title>
<link rel="stylesheet" href="https://fonts.googleapis.com/css2?family=Questrial&display=swap">
<style>
  :root {
    --backdrop: #cfe7df;
    --card-yellow: #e2b81c;
    --card-white: #f7f7f7;
    --card-blue: #31bdd8;
    --brand-orange: #ee6a1c;
    --ink: #2a2f33;
    --rule: #1f2326;
    --cursor-blue: #2a7fd0;
  }
  * { margin: 0; padding: 0; box-sizing: border-box; }
  html, body {
    width: 1200px;
    height: 794px;
    overflow: hidden;
    background: var(--backdrop);
    font-family: "Questrial", "Century Gothic", sans-serif;
  }
  .sheet {
    position: relative;
    width: 1200px;
    height: 794px;
  }
  .card {
    position: absolute;
    top: 242px;
    width: 540px;
    height: 310px;
    border-radius: 30px;
    overflow: hidden;
  }

  /* Front: web address */
  .card--front {
    left: 620px;
    background: var(--card-yellow);
  }
  .web-address {
    position: absolute;
    left: 110px;
    top: 118px;
    font-size: 38px;
    color: var(--brand-orange);
    letter-spacing: 0.5px;
  }
  .web-rule {
    position: absolute;
    left: 110px;
    top: 172px;
    width: 330px;
    height: 2px;
    background: var(--rule);
  }
  .cursor-icon {
    position: absolute;
    left: 432px;
    top: 150px;
    width: 26px;
    height: 30px;
  }

  /* Back: contact details */
  .card--back {
    left: 40px;
    background: var(--card-blue);
  }
  .back-header {
    position: absolute;
    left: 0; top: 0;
    width: 100%;
    height: 140px;
    background: var(--card-white);
    border-bottom: 2px solid var(--rule);
  }
  .brand {
    position: absolute;
    left: 36px;
    top: 76px;
    display: flex;
    align-items: center;
    gap: 10px;
  }
  .brand-mark {
    width: 22px;
    height: 22px;
    background: var(--card-yellow);
  }
  .brand-name {
    font-size: 40px;
    color: var(--brand-orange);
    line-height: 1;
  }
  .holder-name {
    position: absolute;
    right: 44px;
    top: 34px;
    font-size: 22px;
    color: var(--brand-orange);
  }
  .phone {
    position: absolute;
    left: 318px;
    top: 160px;
    display: flex;
    align-items: center;
    gap: 22px;
    font-size: 17px;
    letter-spacing: 1.5px;
    color: var(--ink);
  }
  .phone svg { width: 22px; height: 34px; }
  .address {
    position: absolute;
    left: 36px;
    top: 224px;
    display: flex;
    align-items: center;
    gap: 36px;
    color: var(--ink);
  }
  .address svg { width: 38px; height: 26px; }
  .address p {
    font-size: 15px;
    line-height: 1.25;
  }
</style>
</head>
<body>
<main class="sheet">

  <section class="card card--back" aria-label="Business card, contact side">
    <header class="back-header">
      <div class="brand">
        <span class="brand-mark"></span>
        <span class="brand-name">velbiro</span>
      </div>
      <p class="holder-name">your name</p>
    </header>

    <div class="phone">
      <svg viewBox="0 0 22 34" aria-hidden="true">
        <rect x="1.5" y="1.5" width="19" height="31" rx="3" fill="none" stroke="#2a2f33" stroke-width="2.5"/>
        <line x1="1.5" y1="26" x2="20.5" y2="26" stroke="#2a2f33" stroke-width="2"/>
        <circle cx="11" cy="29.5" r="1.4" fill="#2a2f33"/>
      </svg>
      <span class="phone-number">XXX XXX XXXX</span>
    </div>

    <div class="address">
      <svg viewBox="0 0 38 26" aria-hidden="true">
        <rect x="0" y="0" width="38" height="26" fill="#2a2f33"/>
        <polyline points="1,1 19,15 37,1" fill="none" stroke="#31bdd8" stroke-width="2"/>
      </svg>
      <p>27 Marlow Street,<br>#09-04 Westbrook Tower,<br>Singapore 048216</p>
    </div>
  </section>

  <section class="card card--front" aria-label="Business card, web address side">
    <p class="web-address">www.velbiro.com</p>
    <span class="web-rule"></span>
    <svg class="cursor-icon" viewBox="0 0 26 30" aria-hidden="true">
      <polygon points="2,2 2,24 8,18 12,28 16,26 12,17 20,17" fill="var(--cursor-blue)"/>
    </svg>
  </section>

</main>
</body>
</html>
```